Flyer to acquire new customers for a craft business

Create an A5 (4 pages in total) flyer describing proposed services from a craft business to new customers.

Services are :

All types of renovation (painting, plastering, attaching wallpapers ....)
All types of repairs
Electric repairs
Little to medium woodworks
Services around the house and garden

Flyer must be translatable into several languages beginning with FRENCH.
Texts are being written by ourselves.

Target Market(s)

Private customers

Industry/Entity Type

Mixed craft business

Colors

Designer to choose colors to be used in the design.

```html
<!DOCTYPE html>
<html lang="fr">
<head>
<meta charset="utf-8">
<title>Aren Handwierker – Flyer A5</title>
<link rel="stylesheet" href="https://fonts.googleapis.com/css2?family=Poppins:wght@300;400;500;600&display=swap">
<style>
  :root{
    --ink:#000000;
    --panel:#0b0b0b;
    --stripe-a:#1a1a1a;
    --stripe-b:#2e2e2e;
    --paper:#ffffff;
    --text-light:#e8e8e8;
    --text-muted:#9a9a9a;
    --accent:#e0a526;
    --stage-top:#e9eaed;
    --stage-mid:#dcdde1;
    --photo-warm-a:#8a6a4a;
    --photo-warm-b:#c9a27a;
  }
  *{box-sizing:border-box;margin:0;padding:0}
  html,body{width:1200px;height:4000px;overflow:hidden;background:var(--paper);font-family:'Poppins',sans-serif}
  .canvas{position:relative;width:1200px;height:4000px}
  .stage{position:absolute;left:0;width:1200px}
  .stage--cover{top:0;height:900px;background:var(--stage-top)}
  .stage--inside{top:900px;height:900px;background:linear-gradient(180deg,var(--stage-top),var(--stage-mid))}
  .stage-box{position:absolute;left:194px;top:3070px;width:812px;height:610px;background:var(--stage-mid)}

  .placed{position:absolute;transform-origin:top left}

  /* ---------- cover spread ---------- */
  .cover{position:relative;width:812px;height:573px;background:var(--ink);color:var(--text-light);overflow:hidden}
  .brand{position:absolute;left:468px;top:30px;display:flex;align-items:center;gap:10px}
  .brand-dot{width:34px;height:34px;border-radius:50%;background:var(--accent)}
  .brand-name{font-weight:500;font-size:15px;letter-spacing:1px;color:var(--text-light)}
  .texture{background:linear-gradient(135deg,var(--stripe-b),var(--stripe-a) 55%,var(--stripe-b))}
  .cover-texture-main{position:absolute;left:406px;top:109px;width:406px;height:208px}
  .cover-texture-corner{position:absolute;left:0;top:392px;width:127px;height:181px}
  .title{position:absolute;left:458px;top:328px;line-height:1}
  .title-main{display:block;font-weight:300;font-size:44px;letter-spacing:4px;color:var(--text-light)}
  .title-sub{display:block;margin-top:4px;font-weight:300;font-size:25px;letter-spacing:4px;color:#c9c9c9}
  .contact{position:absolute;left:160px;top:415px;list-style:none;font-size:12px;line-height:1.35}
  .contact li{display:flex;align-items:center;gap:20px;margin-bottom:18px}
  .contact svg{width:22px;height:22px;flex:none;fill:var(--text-light)}
  .web{position:absolute;left:458px;top:512px;display:flex;align-items:center;gap:20px;font-size:12px}
  .web svg{width:20px;height:20px;fill:none;stroke:var(--text-light);stroke-width:1.6}

  /* ---------- inside spread ---------- */
  .inside{display:flex;width:812px;height:573px}
  .page-dark{width:406px;height:573px;background:var(--panel);display:grid;grid-template-columns:1fr 1fr;grid-template-rows:repeat(3,1fr);gap:14px;padding:22px}
  .photo{border-radius:2px}
  .photo--wood{background:linear-gradient(135deg,var(--photo-warm-b),var(--photo-warm-a))}
  .photo--electric{background:linear-gradient(135deg,#d8d2c8,#6b5a44)}
  .photo--tools{background:linear-gradient(135deg,#3a3a3a,#c9a23a)}
  .service{color:var(--text-light);font-size:8.5px;line-height:1.5;padding:4px 2px}
  .service h3{font-weight:600;font-size:10px;letter-spacing:1.5px;margin-bottom:6px;color:var(--paper)}
  .service p{color:#bdbdbd}
  .page-light{width:406px;height:573px;background:var(--paper);display:flex;flex-direction:column}
  .offer{padding:26px 26px 0;flex:1}
  .offer-head{font-size:10px;letter-spacing:2px;color:#111;margin:0 0 12px}
  .offer-head b{font-weight:600}
  .offer-head span{font-weight:300;color:#777}
  .icons{display:flex;gap:18px;margin-bottom:22px;list-style:none}
  .icons li{display:flex;flex-direction:column;align-items:center;gap:5px;width:78px;font-size:8px;font-weight:500;color:#111;text-align:center}
  .icons svg{width:30px;height:30px}
  .photo--kitchen{height:270px;background:linear-gradient(135deg,#5b4636,#b79a7c 55%,#e5e1da)}
</style>
</head>
<body>
<div class="canvas">

  <svg width="0" height="0" style="position:absolute" aria-hidden="true">
    <symbol id="i-pin" viewBox="0 0 24 24"><path d="M12 2a7 7 0 0 0-7 7c0 5 7 13 7 13s7-8 7-13a7 7 0 0 0-7-7zm0 9.5A2.5 2.5 0 1 1 12 6.5a2.5 2.5 0 0 1 0 5z"/></symbol>
    <symbol id="i-phone" viewBox="0 0 24 24"><path d="M6.6 10.8a15 15 0 0 0 6.6 6.6l2.2-2.2a1 1 0 0 1 1-.25 11.4 11.4 0 0 0 3.6.6 1 1 0 0 1 1 1V20a1 1 0 0 1-1 1A17 17 0 0 1 3 4a1 1 0 0 1 1-1h3.5a1 1 0 0 1 1 1c0 1.250.2 2.45.6 3.6a1 1 0 0 1-.25 1z"/></symbol>
    <symbol id="i-mail" viewBox="0 0 24 24"><path d="M3 5h18v14H3zm2 2v.4l7 5 7-5V7zm0 2.8V17h14V9.8l-7 5z"/></symbol>
    <symbol id="c-house" viewBox="0 0 30 30"><circle cx="15" cy="15" r="15" fill="#000"/><path d="M8 15l7-6 7 6v7h-5v-4h-4v4H8z" fill="#fff"/></symbol>
    <symbol id="c-bolt" viewBox="0 0 30 30"><circle cx="15" cy="15" r="15" fill="#000"/><path d="M16 6l-7 11h5l-2 7 8-11h-5z" fill="#fff"/></symbol>
    <symbol id="c-wood" viewBox="0 0 30 30"><circle cx="15" cy="15" r="15" fill="#000"/><rect x="8" y="12" width="14" height="6" fill="#fff"/></symbol>
    <symbol id="c-brush" viewBox="0 0 30 30"><circle cx="15" cy="15" r="15" fill="#000"/><rect x="9" y="8" width="12" height="6" fill="#fff"/><rect x="14" y="14" width="2.5" height="9" fill="#fff"/></symbol>
    <symbol id="c-trowel" viewBox="0 0 30 30"><circle cx="15" cy="15" r="15" fill="#000"/><path d="M8 19l10-10 4 4-10 10z" fill="#fff"/></symbol>
    <symbol id="c-roll" viewBox="0 0 30 30"><circle cx="15" cy="15" r="15" fill="#000"/><rect x="8" y="9" width="14" height="12" rx="2" fill="none" stroke="#fff" stroke-width="2"/></symbol>
    <symbol id="c-hook" viewBox="0 0 30 30"><circle cx="15" cy="15" r="15" fill="#000"/><circle cx="15" cy="15" r="5" fill="none" stroke="#fff" stroke-width="2.5"/></symbol>
  </svg>

  <div class="stage stage--cover"></div>
  <div class="stage stage--inside"></div>
  <div class="stage-box"></div>

  <!-- cover spread, small -->
  <div class="placed" style="left:300px;top:240px;transform:scale(.74)">
    <section class="cover">
      <div class="brand"><span class="brand-dot"></span><span class="brand-name">HAMMERHAUS</span></div>
      <div class="cover-texture-main texture" role="img" aria-label="Diagonal stripe pattern in dark grey"></div>
      <div class="cover-texture-corner texture" role="img" aria-label="Diagonal stripe pattern in dark grey"></div>
      <h1 class="title"><span class="title-main">AREN</span><span class="title-sub">HANDWIERKER</span></h1>
      <ul class="contact">
        <li><svg><use href="#i-pin"/></svg><span>Hammerhaus<br>12, rue des Artisans<br>7340 Bergdorf</span></li>
        <li><svg><use href="#i-phone"/></svg><span>20 40 60 80</span></li>
        <li><svg><use href="#i-mail"/></svg><span>info@hammerhaus.lu</span></li>
      </ul>
      <div class="web"><svg viewBox="0 0 24 24"><circle cx="12" cy="12" r="9"/><path d="M3 12h18M12 3c3 3 3 15 0 18M12 3c-3 3-3 15 0 18"/></svg><span>www.hammerhaus.lu</span></div>
    </section>
  </div>

  <!-- inside spread, medium -->
  <div class="placed" style="left:251px;top:1100px;transform:scale(.86)">
    <section class="inside">
      <div class="page-dark">
        <div class="service"><h3>RENOVATIONS</h3><p>Peinture, plâtrage et pose de papier peint réalisés avec soin pour donner une nouvelle vie à votre intérieur.</p></div>
        <div class="photo photo--wood" role="img" aria-label="Photo of woodworking tools on a workbench"></div>
        <div class="photo photo--electric" role="img" aria-label="Photo of an electrician working on a socket"></div>
        <div class="service"><h3>TRAVAUX EN ÉLECTRICITÉ</h3><p>Installation de prises, luminaires et interrupteurs, dépannage rapide et mise en conformité de votre installation électrique.</p></div>
        <div class="service"><h3>RÉPARATIONS</h3><p>Petites et grandes réparations dans toute la maison, du robinet qui fuit à la porte qui grince.</p></div>
        <div class="photo photo--tools" role="img" aria-label="Photo of hands holding pliers and hand tools"></div>
      </div>
      <div class="page-light">
        <div class="offer">
          <h2 class="offer-head"><b>ALL TYPES</b> <span>OF REPAIRS</span></h2>
          <ul class="icons">
            <li><svg><use href="#c-house"/></svg>Services around the house</li>
            <li><svg><use href="#c-bolt"/></svg>Electric repairs</li>
            <li><svg><use href="#c-wood"/></svg>Little to medium woodworks</li>
          </ul>
          <h2 class="offer-head"><b>ALL TYPES</b> <span>OF RENOVATION</span></h2>
          <ul class="icons">
            <li><svg><use href="#c-hook"/></svg>attaching</li>
            <li><svg><use href="#c-trowel"/></svg>plastering</li>
            <li><svg><use href="#c-roll"/></svg>wallpapers</li>
            <li><svg><use href="#c-brush"/></svg>painting</li>
          </ul>
        </div>
        <div class="photo photo--kitchen" role="img" aria-label="Photo of a craftsman at work in a kitchen"></div>
      </div>
    </section>
  </div>

  <!-- cover spread, full size -->
  <div class="placed" style="left:194px;top:2155px">
    <section class="cover">
      <div class="brand"><span class="brand-dot"></span><span class="brand-name">HAMMERHAUS</span></div>
      <div class="cover-texture-main texture" role="img" aria-label="Diagonal stripe pattern in dark grey"></div>
      <div class="cover-texture-corner texture" role="img" aria-label="Diagonal stripe pattern in dark grey"></div>
      <h1 class="title"><span class="title-main">AREN</span><span class="title-sub">HANDWIERKER</span></h1>
      <ul class="contact">
        <li><svg><use href="#i-pin"/></svg><span>Hammerhaus<br>12, rue des Artisans<br>7340 Bergdorf</span></li>
        <li><svg><use href="#i-phone"/></svg><span>20 40 60 80</span></li>
        <li><svg><use href="#i-mail"/></svg><span>info@hammerhaus.lu</span></li>
      </ul>
      <div class="web"><svg viewBox="0 0 24 24"><circle cx="12" cy="12" r="9"/><path d="M3 12h18M12 3c3 3 3 15 0 18M12 3c-3 3-3 15 0 18"/></svg><span>www.hammerhaus.lu</span></div>
    </section>
  </div>

  <!-- inside spread, small, on grey panel -->
  <div class="placed" style="left:372px;top:3215px;transform:scale(.56)">
    <section class="inside">
      <div class="page-dark">
        <div class="service"><h3>RENOVATIONS</h3><p>Peinture, plâtrage et pose de papier peint réalisés avec soin pour donner une nouvelle vie à votre intérieur.</p></div>
        <div class="photo photo--wood" role="img" aria-label="Photo of woodworking tools on a workbench"></div>
        <div class="photo photo--electric" role="img" aria-label="Photo of an electrician working on a socket"></div>
        <div class="service"><h3>TRAVAUX EN ÉLECTRICITÉ</h3><p>Installation de prises, luminaires et interrupteurs, dépannage rapide et mise en conformité de votre installation électrique.</p></div>
        <div class="service"><h3>RÉPARATIONS</h3><p>Petites et grandes réparations dans toute la maison, du robinet qui fuit à la porte qui grince.</p></div>
        <div class="photo photo--tools" role="img" aria-label="Photo of hands holding pliers and hand tools"></div>
      </div>
      <div class="page-light">
        <div class="offer">
          <h2 class="offer-head"><b>ALL TYPES</b> <span>OF REPAIRS</span></h2>
          <ul class="icons">
            <li><svg><use href="#c-house"/></svg>Services around the house</li>
            <li><svg><use href="#c-bolt"/></svg>Electric repairs</li>
            <li><svg><use href="#c-wood"/></svg>Little to medium woodworks</li>
          </ul>
          <h2 class="offer-head"><b>ALL TYPES</b> <span>OF RENOVATION</span></h2>
          <ul class="icons">
            <li><svg><use href="#c-hook"/></svg>attaching</li>
            <li><svg><use href="#c-trowel"/></svg>plastering</li>
            <li><svg><use href="#c-roll"/></svg>wallpapers</li>
            <li><svg><use href="#c-brush"/></svg>painting</li>
          </ul>
        </div>
        <div class="photo photo--kitchen" role="img" aria-label="Photo of a craftsman at work in a kitchen"></div>
      </div>
    </section>
  </div>

</div>
</body>
</html>
```